Grill, Tunes & Summer Feast.

I need an A3 Poster, Insta Square and Facebook Event Cover photo for a Grill Tunes and Feast Event. Details as follows:

Name: Grill, Tunes and Summer Feast
12pm - Late. Jan 26th at Tallow Creek Taphousing
Acts:
Tin Sparrow - 7pm
Copper Wire & Slow Morris - 3pm - 7pm
Derek Holloway - 12pm -3pm

Free BBQ 2-4pm.

```html
<!DOCTYPE html>
<html lang="en">
<head>
<meta charset="utf-8">
<title>Grill, Tunes &amp; Summer Feast – Event Set</title>
<link rel="stylesheet" href="https://fonts.googleapis.com/css2?family=Oswald:wght@400;500;600&display=swap">
<style>
  :root {
    --navy: #1c2b3a;
    --maroon: #6e3535;
    --paper: #ffffff;
    --backdrop: #e8e8e6;
    --shadow: rgba(0, 0, 0, 0.14);
  }
  * { margin: 0; padding: 0; box-sizing: border-box; }
  html, body {
    width: 1099px; height: 1200px; overflow: hidden;
    background: var(--backdrop);
    font-family: "Oswald", "Arial Narrow", sans-serif;
    color: var(--navy);
  }
  .sprites { position: absolute; width: 0; height: 0; }
  .stage { position: relative; width: 1099px; height: 1200px; }

  .sheet {
    position: absolute;
    background: var(--paper);
    box-shadow: 0 14px 10px -10px var(--shadow);
  }
  .sheet--cover  { left: 130px; top: 121px; width: 839px; height: 311px; }
  .sheet--poster { left: 130px; top: 485px; width: 401px; height: 567px; }
  .sheet--square { left: 564px; top: 485px; width: 405px; height: 405px; }

  .emblem { position: absolute; display: block; overflow: visible; }
  .emblem__title { fill: var(--navy); font-family: "Oswald", sans-serif; font-weight: 500; font-size: 62px; letter-spacing: 4px; text-transform: uppercase; }
  .emblem__art { fill: var(--navy); }

  .sheet--cover .emblem  { left: 47px; top: 31px; width: 256px; height: 256px; }
  .sheet--poster .emblem { left: 21px; top: 33px; width: 345px; height: 345px; }
  .sheet--square .emblem { left: 76px; top: 34px; width: 226px; height: 226px; }

  .rule-v { position: absolute; width: 1px; background: var(--navy); }
  .sheet--cover .rule-v  { left: 367px; top: 26px; height: 258px; }
  .sheet--poster .rule-v { left: 185px; top: 465px; height: 76px; }
  .sheet--square .rule-v { left: 192px; top: 319px; height: 73px; }

  .venue-mark {
    position: absolute;
    font-weight: 600; text-transform: uppercase; color: var(--navy);
    text-align: center; line-height: 1.02; letter-spacing: 0.06em;
  }
  .sheet--cover .venue-mark  { left: 519px; top: 14px; width: 149px; font-size: 22px; }
  .sheet--poster .venue-mark { left: 33px; top: 470px; width: 132px; font-size: 25px; }
  .sheet--square .venue-mark { left: 37px; top: 324px; width: 126px; font-size: 24px; }

  .free-bbq {
    position: absolute; color: var(--maroon); font-weight: 400;
    text-align: center; white-space: nowrap; transform: translateX(-50%);
  }
  .sheet--cover .free-bbq  { left: 594px; top: 264px; font-size: 20px; }
  .sheet--poster .free-bbq { left: 200px; top: 392px; font-size: 28px; }
  .sheet--square .free-bbq { left: 202px; top: 278px; font-size: 20px; }

  .details { position: absolute; }
  .sheet--cover .details  { left: 445px; top: 102px; width: 298px; font-size: 44px; }
  .sheet--poster .details { left: 208px; top: 468px; width: 162px; font-size: 22px; }
  .sheet--square .details { left: 218px; top: 320px; width: 152px; font-size: 20px; }

  .details__when { font-weight: 400; line-height: 1.0; white-space: nowrap; letter-spacing: -0.01em; }
  .details__where {
    display: flex; align-items: center; gap: 0.3em;
    font-size: 0.41em; white-space: nowrap; margin-top: 0.15em;
  }
  .details__where::before, .details__where::after {
    content: ""; flex: 1; height: 1px; background: var(--navy);
  }
  .details__where::before { margin-right: 0.45em; }
  .details__where::after { margin-left: 0.45em; }

  .acts { display: flex; align-items: center; margin-top: 0.35em; }
  .acts__label { font-size: 0.57em; width: 2.42em; flex: none; }
  .acts__list { list-style: none; font-size: 0.38em; line-height: 1.35; }
  .acts__item { display: flex; align-items: center; gap: 0.35em; white-space: nowrap; }
  .acts__icon { width: 0.95em; height: 0.8em; flex: none; }
</style>
</head>
<body>
<svg class="sprites" aria-hidden="true">
  <defs>
    <symbol id="note-icon" viewBox="0 0 14 12">
      <path d="M4 2 L13 0 M4 2 L4 9 M13 0 L13 7" stroke="currentColor" stroke-width="1.3" fill="none"/>
      <ellipse cx="2.6" cy="9.6" rx="2" ry="1.5" fill="none" stroke="currentColor" stroke-width="1.1"/>
      <ellipse cx="11.6" cy="7.6" rx="2" ry="1.5" fill="none" stroke="currentColor" stroke-width="1.1"/>
    </symbol>
    <symbol id="event-emblem" viewBox="-215 -215 430 430" overflow="visible">
      <path id="arc-top" d="M -131.6 47.9 A 140 140 0 1 1 131.6 47.9" fill="none"/>
      <path id="arc-bottom" d="M -183.2 -66.7 A 195 195 0 1 0 183.2 -66.7" fill="none"/>
      <circle class="emblem__art" cx="0" cy="0" r="121" role="img" aria-label="Line drawings of a speaker, guitar, microphone, beer mug, grill and sausage"/>
      <text class="emblem__title"><textPath href="#arc-top" startOffset="50%" text-anchor="middle">Grill, Tunes</textPath></text>
      <text class="emblem__title"><textPath href="#arc-bottom" startOffset="50%" text-anchor="middle">&amp; Summer Feast</textPath></text>
    </symbol>
  </defs>
</svg>

<main class="stage">

  <section class="sheet sheet--cover" aria-label="Event cover">
    <svg class="emblem" role="img" aria-label="Grill, Tunes &amp; Summer Feast"><use href="#event-emblem"/></svg>
    <div class="rule-v"></div>
    <div class="venue-mark">Tallow Creek<br>Taphouse</div>
    <div class="details">
      <p class="details__when">12pm - Late. Jan 26th</p>
      <p class="details__where">at Tallow Creek Taphousing</p>
      <div class="acts">
        <span class="acts__label">ACTS:</span>
        <ul class="acts__list">
          <li class="acts__item"><svg class="acts__icon"><use href="#note-icon"/></svg>Tin Sparrow - 7pm</li>
          <li class="acts__item"><svg class="acts__icon"><use href="#note-icon"/></svg>Copper Wire &amp; Slow Morris - 3pm - 7pm</li>
          <li class="acts__item"><svg class="acts__icon"><use href="#note-icon"/></svg>Derek Holloway - 12pm - 3pm</li>
        </ul>
      </div>
    </div>
    <p class="free-bbq">Free BBQ 2-4pm</p>
  </section>

  <section class="sheet sheet--poster" aria-label="A3 poster">
    <svg class="emblem" role="img" aria-label="Grill, Tunes &amp; Summer Feast"><use href="#event-emblem"/></svg>
    <p class="free-bbq">Free BBQ 2-4pm</p>
    <div class="venue-mark">Tallow Creek<br>Taphouse</div>
    <div class="rule-v"></div>
    <div class="details">
      <p class="details__when">12pm - Late. Jan 26th</p>
      <p class="details__where">at Tallow Creek Taphousing</p>
      <div class="acts">
        <span class="acts__label">ACTS:</span>
        <ul class="acts__list">
          <li class="acts__item"><svg class="acts__icon"><use href="#note-icon"/></svg>Tin Sparrow - 7pm</li>
          <li class="acts__item"><svg class="acts__icon"><use href="#note-icon"/></svg>Copper Wire &amp; Slow Morris - 3pm - 7pm</li>
          <li class="acts__item"><svg class="acts__icon"><use href="#note-icon"/></svg>Derek Holloway - 12pm - 3pm</li>
        </ul>
      </div>
    </div>
  </section>

  <section class="sheet sheet--square" aria-label="Square social post">
    <svg class="emblem" role="img" aria-label="Grill, Tunes &amp; Summer Feast"><use href="#event-emblem"/></svg>
    <p class="free-bbq">Free BBQ 2-4pm</p>
    <div class="venue-mark">Tallow Creek<br>Taphouse</div>
    <div class="rule-v"></div>
    <div class="details">
      <p class="details__when">12pm - Late. Jan 26th</p>
      <p class="details__where">at Tallow Creek Taphousing</p>
      <div class="acts">
        <span class="acts__label">ACTS:</span>
        <ul class="acts__list">
          <li class="acts__item"><svg class="acts__icon"><use href="#note-icon"/></svg>Tin Sparrow - 7pm</li>
          <li class="acts__item"><svg class="acts__icon"><use href="#note-icon"/></svg>Copper Wire &amp; Slow Morris - 3pm - 7pm</li>
          <li class="acts__item"><svg class="acts__icon"><use href="#note-icon"/></svg>Derek Holloway - 12pm - 3pm</li>
        </ul>
      </div>
    </div>
  </section>

</main>
</body>
</html>
```